Garage Flooring Flyer

We are looking for a flyer design for our garage flooring company. We specialise in installing garage floor coatings. We use industrial grade products and are serious about durability and quality.
We target male car enthusiasts and want to project the image of a modern high-tech company. The flyer should be stunningly visual and incorporate the logo and photos we have attached. Other photos or images are welcomed.
Some key mentions to be made on the flyer are listed below:
About Us
"We are K*** R***** LLC, Home of the garage enthusiasts and Waukesha’s premier garage floor installer"
Services
Garage Floor Coatings
Offers
-Call or Email for a FREE estimate!
Credentials
-QN logo
-Pictavo Logo
-Zorbin Logo
-5stars?
Benefit Highlights to be mentioned or listed (not in any particular order)
-Industrial Quality and Strength
-Easy to Clean
-Many Color Options
-Locally Owned and Operated
-Satisfaction Guaranteed
-Lifetime Limited Warranty
-Increases Home Value
-MAKE YOUR FRIENDS AND NEIGHBORS JEALOUS!
-Fully Insured
-Certified and Trusted Installer
-Oil and Chemical Resistant
-UV Stable
-Impact and Abrasion Resistant
Contact Info
-Phone
-Email
-Website
Captions
-"From diamond grinding surface prep to using only the highest industrial-grade products, we believe in taking the time to ensure a proper installation and guarantee a durable long-lasting and beautiful garage floor";
-Serving Southeastern Wisconsin!

```html
<!DOCTYPE html>
<html lang="en">
<head>
<meta charset="utf-8">
<title>Kord Rydell Garage Flooring Flyer</title>
<link rel="stylesheet" href="https://fonts.googleapis.com/css2?family=Raleway:wght@400;500;600;700;800&family=Open+Sans:wght@400;600&display=swap">
<style>
:root{
  --teal:#2a8db4;
  --teal-light:#3fa6cc;
  --indigo:#3b48a0;
  --indigo-deep:#2f3a8c;
  --white:#ffffff;
  --gold:#f2c230;
  --stage:#e4e4e6;
  --photo-a:#9aa3ad;
  --photo-b:#d8dcdf;
}
*{box-sizing:border-box;margin:0;padding:0}
html,body{width:1200px;height:972px;overflow:hidden}
body{background:var(--stage);position:relative;font-family:"Open Sans",Arial,sans-serif;color:var(--white)}
.flyer{position:absolute;top:86px;width:538px;height:695px;overflow:hidden;box-shadow:0 14px 18px rgba(0,0,0,.18)}
.flyer--front{left:44px;background:var(--teal)}
.flyer--back{left:600px;background:var(--indigo)}
.brand{position:absolute;font-family:"Raleway",Arial,sans-serif;font-weight:800;color:var(--white);text-align:center;line-height:1}
.brand__name{display:block;font-size:34px;letter-spacing:1px}
.brand__sub{display:block;font-size:16px;letter-spacing:8px;margin-top:4px}
.photo{position:absolute;background:linear-gradient(135deg,var(--photo-a),var(--photo-b) 55%,#7d858e)}
.tab{position:absolute;font-family:"Raleway",Arial,sans-serif;color:var(--white);display:flex;align-items:center}

/* front */
.front__top{position:absolute;left:0;top:0;width:538px;height:200px;background:var(--teal-light)}
.front__brand{left:18px;top:24px}
.front__stars{position:absolute;left:30px;top:88px;display:flex}
.front__intro{position:absolute;left:204px;width:330px;top:30px;text-align:center;font-family:"Raleway",Arial,sans-serif;font-size:13px;line-height:1.4}
.front__intro .lead{font-size:16px}
.front__intro strong{font-size:19px;font-weight:500}
.front__hero{position:absolute;left:-40px;top:118px;width:618px;height:332px;border-radius:50%;border:7px solid var(--indigo);overflow:hidden;background:var(--indigo)}
.front__hero .photo{inset:0}
.ribbon{position:absolute;left:358px;top:128px;width:60px;height:224px}
.badge{position:absolute;left:339px;top:180px;width:98px;height:98px;border-radius:50%;background:var(--indigo);border:3px dashed var(--white);display:flex;flex-direction:column;align-items:center;justify-content:center;text-align:center;line-height:1.1;font-size:9px}
.badge__free{font-family:"Raleway",Arial,sans-serif;font-weight:800;font-size:20px;margin:2px 0}
.service-pill{position:absolute;left:140px;top:400px;width:266px;height:22px;border-radius:11px;background:var(--indigo);font-family:"Raleway",Arial,sans-serif;font-weight:700;font-size:11px;letter-spacing:3px;display:flex;align-items:center;justify-content:center}
.tab--benefit{left:0;top:433px;width:130px;height:30px;padding-left:6px;background:var(--indigo);clip-path:polygon(0 0,100% 0,88% 100%,0 100%);font-size:20px;letter-spacing:4px;font-weight:500}
.benefit-list{position:absolute;left:6px;top:472px;list-style:none;font-family:"Raleway",Arial,sans-serif;font-size:13px}
.benefit-list li{height:26.8px;display:flex;align-items:center;gap:6px}
.tab--jealous{left:358px;top:468px;width:180px;height:43px;background:var(--indigo);clip-path:polygon(6% 0,100% 0,100% 100%,0 100%);flex-direction:column;justify-content:center;font-weight:700;font-size:8px;text-align:center;line-height:1.2}
.tab--jealous b{font-size:15px;font-weight:800}
.perk-list{position:absolute;right:10px;top:522px;list-style:none;font-family:"Raleway",Arial,sans-serif;font-size:16px;text-align:right}
.perk-list li{height:23.5px;display:flex;align-items:center;justify-content:flex-end;gap:6px}
.front__footer{position:absolute;left:0;bottom:0;width:538px;height:27px;background:var(--indigo);display:flex;align-items:center;padding:0 12px;font-family:"Raleway",Arial,sans-serif;font-size:13px;letter-spacing:.5px}
.socials{display:flex;gap:10px;font-size:10px;font-weight:600}
.socials span{display:flex;align-items:center;gap:3px}
.socials i{display:inline-block;width:8px;height:8px;border-radius:50%;background:var(--white)}
.front__footer .email{margin-left:auto}

/* back */
.back__band{position:absolute;left:0;top:0;width:538px;height:200px}
.back__title{position:absolute;left:12px;top:16px;font-family:"Raleway",Arial,sans-serif;font-weight:600}
.back__title small{display:block;font-size:16px;letter-spacing:6px}
.back__title span{display:block;font-size:34px;letter-spacing:4px;margin-top:6px}
.back__rule{position:absolute;left:26px;top:100px;width:142px;height:2px;background:var(--white)}
.back__rule--short{left:78px;top:94px;width:56px}
.back__brand{left:348px;top:24px}
.tab--contact{left:0;top:150px;width:158px;height:28px;padding-left:8px;background:var(--teal);clip-path:polygon(0 0,100% 0,88% 100%,0 100%);font-weight:700;font-size:13px;letter-spacing:2px}
.contact-list{position:absolute;left:8px;top:188px;list-style:none;font-size:11.5px;font-weight:600}
.contact-list li{height:31px;display:flex;align-items:center;gap:8px}
.frame{position:absolute;border:7px solid var(--white);border-radius:22px;overflow:hidden;box-shadow:0 4px 10px rgba(0,0,0,.3)}
.frame .photo{inset:0}
.tab--caption{left:0;top:528px;width:166px;height:36px;padding-left:8px;background:var(--teal);clip-path:polygon(0 0,100% 0,88% 100%,0 100%);font-weight:700;font-size:17px;letter-spacing:5px}
.caption{position:absolute;left:6px;top:590px;width:400px;font-size:9.5px;line-height:1.5}
.back__footer{position:absolute;left:0;bottom:0;width:538px;height:24px;background:var(--teal);display:flex;align-items:center;justify-content:center;font-family:"Raleway",Arial,sans-serif;font-size:13px;letter-spacing:2px}
</style>
</head>
<body>

<section class="flyer flyer--front">
  <div class="front__top"></div>
  <div class="brand front__brand"><span class="brand__name">KORD</span><span class="brand__sub">RYDELL</span></div>
  <div class="front__stars" aria-label="Five stars">
    <svg width="110" height="20" viewBox="0 0 98 18" fill="var(--gold)">
      <polygon points="9,0 11.6,6 18,6.5 13,10.7 14.6,17 9,13.5 3.4,17 5,10.7 0,6.5 6.4,6"/>
      <polygon transform="translate(20,0)" points="9,0 11.6,6 18,6.5 13,10.7 14.6,17 9,13.5 3.4,17 5,10.7 0,6.5 6.4,6"/>
      <polygon transform="translate(40,0)" points="9,0 11.6,6 18,6.5 13,10.7 14.6,17 9,13.5 3.4,17 5,10.7 0,6.5 6.4,6"/>
      <polygon transform="translate(60,0)" points="9,0 11.6,6 18,6.5 13,10.7 14.6,17 9,13.5 3.4,17 5,10.7 0,6.5 6.4,6"/>
      <polygon transform="translate(80,0)" points="9,0 11.6,6 18,6.5 13,10.7 14.6,17 9,13.5 3.4,17 5,10.7 0,6.5 6.4,6"/>
    </svg>
  </div>
  <p class="front__intro"><span class="lead">We are <strong>KORD RYDELL LLC,</strong></span><br>Home of the garage enthusiasts and Waukesha's<br>premier garage floor installer</p>

  <div class="front__hero">
    <div class="photo" role="img" aria-label="Photo of a finished garage with a sports car on a lift over a speckled coated floor"></div>
  </div>

  <svg class="ribbon" viewBox="0 0 60 224" aria-hidden="true">
    <polygon points="0,0 60,0 60,224 30,198 0,224" fill="var(--indigo)"/>
  </svg>
  <div class="badge"><span>Call or Email<br>for a</span><span class="badge__free">FREE</span><span>estimate!</span></div>
  <div class="service-pill">GARAGE FLOOR COATINGS</div>

  <div class="tab tab--benefit">BENEFIT</div>
  <ul class="benefit-list">
    <li><svg width="10" height="10" viewBox="0 0 10 10"><path d="M1 5h7M5 2l3 3-3 3" stroke="#fff" fill="none"/></svg>Industrial Quality and Strength</li>
    <li><svg width="10" height="10" viewBox="0 0 10 10"><path d="M1 5h7M5 2l3 3-3 3" stroke="#fff" fill="none"/></svg>Easy to Clean</li>
    <li><svg width="10" height="10" viewBox="0 0 10 10"><path d="M1 5h7M5 2l3 3-3 3" stroke="#fff" fill="none"/></svg>Many Color Options</li>
    <li><svg width="10" height="10" viewBox="0 0 10 10"><path d="M1 5h7M5 2l3 3-3 3" stroke="#fff" fill="none"/></svg>Locally Owned and Operated</li>
    <li><svg width="10" height="10" viewBox="0 0 10 10"><path d="M1 5h7M5 2l3 3-3 3" stroke="#fff" fill="none"/></svg>Satisfaction Guaranteed</li>
    <li><svg width="10" height="10" viewBox="0 0 10 10"><path d="M1 5h7M5 2l3 3-3 3" stroke="#fff" fill="none"/></svg>Lifetime Limited Warranty</li>
    <li><svg width="10" height="10" viewBox="0 0 10 10"><path d="M1 5h7M5 2l3 3-3 3" stroke="#fff" fill="none"/></svg>Increases Home Value</li>
  </ul>

  <div class="tab tab--jealous">MAKE YOUR<br>FRIENDS AND NEIGHBORS<b>JEALOUS!</b></div>
  <ul class="perk-list">
    <li>Fully Insured<svg width="11" height="11" viewBox="0 0 10 10"><path d="M1 5l3 3 5-6" stroke="#fff" fill="none" stroke-width="1.4"/></svg></li>
    <li>Certified and Trusted Installer<svg width="11" height="11" viewBox="0 0 10 10"><path d="M1 5l3 3 5-6" stroke="#fff" fill="none" stroke-width="1.4"/></svg></li>
    <li>Oil and Chemical Resistant<svg width="11" height="11" viewBox="0 0 10 10"><path d="M1 5l3 3 5-6" stroke="#fff" fill="none" stroke-width="1.4"/></svg></li>
    <li>UV Stable<svg width="11" height="11" viewBox="0 0 10 10"><path d="M1 5l3 3 5-6" stroke="#fff" fill="none" stroke-width="1.4"/></svg></li>
    <li>Impact and Abrasion Resistant<svg width="11" height="11" viewBox="0 0 10 10"><path d="M1 5l3 3 5-6" stroke="#fff" fill="none" stroke-width="1.4"/></svg></li>
  </ul>

  <footer class="front__footer">
    <div class="socials"><span><i></i>QN</span><span><i></i>Pictavo</span><span><i></i>Zorbin</span></div>
    <span class="email">FloorCoatings@Mailvo.com</span>
  </footer>
</section>

<section class="flyer flyer--back">
  <svg class="back__band" viewBox="0 0 538 200" aria-hidden="true">
    <path d="M0 0H538V132C470 150 420 140 360 150C300 160 260 130 230 120C200 110 150 118 110 120H0Z" fill="var(--teal)"/>
    <path d="M0 0H340C300 20 270 60 250 100C230 130 180 124 120 122H0Z" fill="var(--indigo-deep)"/>
  </svg>
  <div class="back__title"><small>GARAGE FLOOR</small><span>COATINGS</span></div>
  <div class="back__rule back__rule--short"></div>
  <div class="back__rule"></div>
  <div class="brand back__brand"><span class="brand__name">KORD</span><span class="brand__sub">RYDELL</span></div>

  <div class="tab tab--contact">CONTACT INFO</div>
  <ul class="contact-list">
    <li><svg width="12" height="12" viewBox="0 0 12 12"><path d="M2 1l2 0 1 3-1.5 1a7 7 0 0 0 3.5 3.5L8 7l3 1v2c0 1-1 1-1 1A9 9 0 0 1 1 2s0-1 1-1z" fill="#fff"/></svg>555-014-7788</li>
    <li><svg width="12" height="12" viewBox="0 0 12 12" fill="none" stroke="#fff"><circle cx="6" cy="6" r="5"/><path d="M1 6h10M6 1c3 3 3 7 0 10M6 1c-3 3-3 7 0 10"/></svg>www.FloorCoatingsPro.com</li>
    <li><svg width="12" height="12" viewBox="0 0 12 12" fill="none" stroke="#fff"><rect x="1" y="3" width="10" height="7"/><path d="M1 3l5 4 5-4"/></svg>FloorCoatings@Mailvo.com</li>
  </ul>

  <div class="frame" style="left:236px;top:124px;width:288px;height:254px">
    <div class="photo" role="img" aria-label="Photo of a bright modern garage with a two-post lift and grey speckled floor"></div>
  </div>
  <div class="frame" style="left:106px;top:316px;width:211px;height:192px">
    <div class="photo" style="background:linear-gradient(135deg,#e0b92c,#5b5f66 60%,#2f3338)" role="img" aria-label="Photo of a yellow sports car raised on a garage lift"></div>
  </div>
  <div class="frame" style="left:293px;top:385px;width:230px;height:208px">
    <div class="photo" style="background:linear-gradient(160deg,#5a7fa6,#8fa3b8 45%,#b9c2cc)" role="img" aria-label="Close photo of a blue car wheel resting on a speckled coated floor"></div>
  </div>

  <div class="tab tab--caption">CAPTIONS</div>
  <p class="caption">"From diamond grinding surface prep to using only<br>the highest industrial-grade products,<br>we believe in taking the time to ensure a proper installation and guarantee<br>a durable long-lasting and beautiful garage floor"</p>

  <footer class="back__footer">Serving Southeastern Wisconsin!</footer>
</section>

</body>
</html>
```